Web Design Project - Shipping Industry

Goals and Objectives
The objective of the new website is to create a more modern look and feel. The site will also allow for a more effective means of communicating with members while providing the public with information and developments in the local, regional and international shipping industry.
Scope
The website will highlight the history of the organisation inclusive of text and photographs. It will take visitors through the years from beginning to present. Information on the history of the shipping industry will also be included.
It will feature current articles on the organisation, its members and stakeholders in the shipping industry. Member information as well as pertinent details regarding the organisation’s subsidiaries will be documented for the website.
Information as it relates to shipping statistics, case studies, laws and regulations, international treaties and trade documents, shipping terms, careers in shipping, job opportunities, training opportunities, information for shippers including port listing and trade lanes will be main features of the content for the website.
The Association’s community involvement, industry calendar events and related links relevant industry members will also be featured.
Target Market
• The General Public;
• Members of the organization;
• Shipping Industry Stakeholders (local, regional and international);
• Tertiary students conducting research.
• Potential employees
• Potential Business Partners
Best Practice Bench Marketing
The following websites are being looked at:
• Velloric Docks - http://www.vellori-docks.example/ (preferred look)
• Corvane Maritime Association - http://www.cmx-assoc.example/ (like image transition on main page)
• Trovald - http://www.trovald.example (professional look)
• KBU - http://www.quaylinx.example (preferred color: blue in logo)
• Wuzo - http://www.wuzo.example/electronics/tv-video-audio/ (preferred look for links page: image + short text below + visit site link)
Expected Result
• 3 - 5 pages which must include: [1] main page [2] standard page [3] links page
Target Market(s)
The General Public; Members of the organization; Shipping Industry Stakeholders (local, regional and international); Tertiary students conductin
Industry/Entity Type
Shipping
Look and feel

```html
<!DOCTYPE html>
<html lang="en">
<head>
<meta charset="utf-8">
<title>The Harbourline Shipping Association – About Us</title>
<link href="https://fonts.googleapis.com/css2?family=Questrial&family=Noto+Sans:wght@400;700&family=Sorts+Mill+Goudy&display=swap" rel="stylesheet">
<style>
:root{
  --navy:#1d2a78;
  --blue:#1f5bb5;
  --band:#0d4aa6;
  --band-dark:#0a3a8a;
  --orange:#f29b00;
  --orange-bright:#ffa500;
  --side:#d5ddef;
  --text:#333;
  --muted:#666;
  --rule:#cfcfcf;
  --footer:#c8c8c8;
}
*{box-sizing:border-box;margin:0;padding:0}
html,body{width:1008px;height:1200px;overflow:hidden;background:#fff}
body{position:relative;font-family:"Noto Sans",sans-serif;color:var(--text)}
.abs{position:absolute}
a{text-decoration:none;color:inherit}

.brand-mark{left:100px;top:26px;width:70px;height:70px;border-radius:50%;background:var(--blue)}
.brand-name{left:100px;top:98px;font-family:"Sorts Mill Goudy",serif;font-size:20px;color:var(--navy)}

.login-label{left:403px;top:23px;font-family:"Questrial",sans-serif;font-size:11px;letter-spacing:.5px;color:var(--navy)}
.field{top:18px;width:160px;height:22px;border:2px solid #d6d6d6;border-radius:11px;font-size:9.5px;color:#888;padding:4px 12px}
.field.user{left:506px}
.field.pass{left:675px}
.login-btn{left:848px;top:18px;width:59px;height:21px;background:var(--orange);border-radius:3px;color:#fff;font-family:"Sorts Mill Goudy",serif;font-size:11px;text-align:center;line-height:21px;letter-spacing:.5px}
.account{top:53px;font-size:9.5px;color:#333}
.account.register{left:738px}
.account.forgot{left:818px}
.account-sep{left:800px;top:51px;width:1px;height:17px;background:#999}

.main-nav a{position:absolute;top:153px;font-family:"Questrial",sans-serif;font-size:11px;color:var(--blue)}
.main-nav a.active{color:#e2541d}

.band{left:100px;top:193px;width:806px;height:53px;background:var(--band)}
.band-label{left:125px;top:211px;font-family:"Questrial",sans-serif;font-weight:bold;font-size:11px;color:#fff;letter-spacing:.3px}
.band-text{left:255px;top:212px;font-family:"Questrial",sans-serif;font-size:9.5px;color:#fff;letter-spacing:.4px}
.search{left:709px;top:193px;width:197px;height:53px;background:var(--band-dark)}
.search-label{left:769px;top:200px;font-family:"Questrial",sans-serif;font-size:10px;color:#ffc400}
.search-input{left:726px;top:219px;width:167px;height:18px;background:#fff;border-radius:9px}
.search-btn{left:866px;top:219px;width:27px;height:18px;background:var(--orange);border-radius:9px}

.sidebar{left:100px;top:246px;width:182px;height:666px;background:var(--side)}
.side-nav a{position:absolute;left:123px;font-family:"Questrial",sans-serif;font-size:11px;color:var(--blue)}
.side-home{left:100px;top:294px;width:182px;height:24px;background:var(--orange-bright)}
.side-nav a.current{color:#fff}
.side-title{left:110px;font-family:"Questrial",sans-serif;font-size:14px;color:#444}
.side-list a{position:absolute;left:133px;font-size:9.5px;color:var(--orange);letter-spacing:.4px}
.side-list i{position:absolute;left:120px;width:6px;height:6px;border:1.5px solid var(--orange);border-radius:50%}

.crumb{left:307px;top:262px;font-size:9.5px;color:#777}
.crumb b{font-weight:400;color:#333}
.page-title{left:307px;top:290px;font-family:"Questrial",sans-serif;font-size:22px;font-weight:400;color:var(--navy);letter-spacing:.5px}
.section-title{left:307px;font-family:"Questrial",sans-serif;font-size:15px;font-weight:400;color:var(--orange)}
.rule{left:307px;width:618px;height:1px;background:var(--rule)}
.copy{left:307px;width:605px;font-size:9.3px;line-height:11.2px;color:#333}

.photo{left:304px;top:633px;width:308px;height:155px;border:2px solid #b7b7b7;background:linear-gradient(135deg,#8fa9d8,#c9d6ee 55%,#7f9dd1)}
.checks li{position:absolute;left:651px;list-style:none;font-size:9.8px;color:#333;padding-left:20px}
.checks svg{position:absolute;left:0;top:0}

.rule-bottom{left:100px;top:912px;width:806px;height:1px;background:var(--rule)}
.partner{top:950px;font-family:"Questrial",sans-serif;font-size:14px;color:#333;display:flex;align-items:center;gap:6px}
.partner i{display:inline-block;width:14px;height:14px;background:#1f5bb5}

.footer{left:0;top:1027px;width:1008px;height:173px;background:var(--footer)}
.footer-nav a{position:absolute;top:1051px;font-family:"Questrial",sans-serif;font-size:10px;color:var(--navy)}
.footer-mark{left:101px;top:1088px;width:46px;height:46px;border-radius:50%;background:var(--blue)}
.footer-name{left:101px;top:1138px;font-family:"Sorts Mill Goudy",serif;font-size:14px;color:var(--navy)}
.copyright{left:101px;top:1164px;font-family:"Questrial",sans-serif;font-size:9.5px;color:#555}
.connect-title{left:687px;top:1047px;font-family:"Questrial",sans-serif;font-size:14px;color:#444;letter-spacing:.4px}
.feed{left:685px;top:1069px;width:222px;height:73px;background:#fff;padding:9px 13px;font-size:8.3px;line-height:10px;color:#333}
.feed-meta{margin-top:7px;color:#e2541d;font-size:8.5px;padding-left:4px}
.feed-meta em{margin-left:8px}
.social{top:1147px;width:24px;height:24px;border-radius:50%;background:#2166b8;border:2px solid #fff}
</style>
</head>
<body>

<header>
  <div class="abs brand-mark" aria-hidden="true"></div>
  <div class="abs brand-name">The Harbourline Shipping Association</div>

  <div class="abs login-label">MEMBER LOGIN:</div>
  <div class="abs field user">User ID</div>
  <div class="abs field pass">Password</div>
  <div class="abs login-btn">LOG IN</div>
  <a class="abs account register" href="#">Register</a>
  <div class="abs account-sep"></div>
  <a class="abs account forgot" href="#">Forgot password?</a>

  <nav class="main-nav">
    <a class="active" href="#" style="left:101px">ABOUT US</a>
    <a href="#" style="left:178px">SHIPPING SCHEDULE</a>
    <a href="#" style="left:307px">NEWS</a>
    <a href="#" style="left:358px">FAQ</a>
    <a href="#" style="left:402px">CONTACT US</a>
    <a href="#" style="left:499px">CANINE SERVICES</a>
    <a href="#" style="left:618px">NAUTIVEX</a>
    <a href="#" style="left:706px">LINKS</a>
  </nav>
</header>

<section class="announcements">
  <div class="abs band"></div>
  <div class="abs band-label">ANNOUNCEMENTS:</div>
  <div class="abs band-text">WELCOME TO THE KBU'S WEBSITE: WE WORK THE PORT OF CALDERRA...</div>
  <div class="abs search"></div>
  <div class="abs search-label">SEARCH SITE</div>
  <div class="abs search-input"></div>
  <div class="abs search-btn"></div>
  <svg class="abs" style="left:872px;top:221px" width="14" height="14" viewBox="0 0 14 14" aria-hidden="true">
    <circle cx="5.5" cy="5.5" r="3.8" fill="none" stroke="#fff" stroke-width="1.6"/>
    <line x1="8.3" y1="8.3" x2="12.5" y2="12.5" stroke="#fff" stroke-width="2"/>
  </svg>
</section>

<aside>
  <div class="abs sidebar"></div>
  <div class="abs side-home"></div>
  <svg class="abs" style="left:110px;top:301px" width="8" height="11" viewBox="0 0 8 11" aria-hidden="true"><polyline points="1,1 6,5.5 1,10" fill="none" stroke="#333" stroke-width="1.2"/></svg>
  <nav class="side-nav">
    <a class="current" href="#" style="top:299px">HOME</a>
    <a href="#" style="top:324px">ABOUT US</a>
    <a href="#" style="top:349px">HOW WE WORK</a>
    <a href="#" style="top:374px">OUR SERVICES</a>
    <a href="#" style="top:399px">WHY US</a>
    <a href="#" style="top:424px">NEWS AND UPDATES</a>
    <a href="#" style="top:450px">ABOUT ORGANISATIONS</a>
    <a href="#" style="top:475px">ABOUT MEMBERS</a>
    <a href="#" style="top:500px">FAQS</a>
    <a href="#" style="top:525px">CONTACT US</a>
  </nav>

  <h3 class="abs side-title" style="top:589px;font-weight:400">Links</h3>
  <div class="side-list">
    <i style="top:619px"></i><a href="#" style="top:615px">Training Courses</a>
    <i style="top:634px"></i><a href="#" style="top:630px">About the Port of Calderra</a>
    <i style="top:649px"></i><a href="#" style="top:645px">Open Tenders</a>
  </div>

  <h3 class="abs side-title" style="top:699px;font-weight:400">Important Facts</h3>
  <div class="side-list">
    <i style="top:729px"></i><a href="#" style="top:725px">Laws and Legislation</a>
    <i style="top:744px"></i><a href="#" style="top:740px">International trade Docs</a>
    <i style="top:759px"></i><a href="#" style="top:755px">Port Statistics</a>
    <i style="top:774px"></i><a href="#" style="top:770px">Shipping Terms</a>
  </div>
</aside>

<main>
  <div class="abs crumb">Home &gt; <b>About Us</b></div>
  <h1 class="abs page-title">ABOUT US</h1>

  <h2 class="abs section-title" style="top:360px">About Us</h2>
  <div class="abs rule" style="top:386px"></div>
  <p class="abs copy" style="top:400px">Fusce quis lacus diam, sit amet sollicitudin ante. Quisque ultricies dolor sit amet enim malesuada consectetur. Maecenas vulputate tellus nec orci posuere interdum. Suspendisse potenti. Fusce qis enim massa. Ut tempor turpis non dolor feugiat vel tempus ligula malesuada nibh erat, euismod ac interdum non, lacinia eu massa. Maecenas vulputate tellus nec orci posuere interdum. Suspendisse potenti. Fusce qis enim massa. Ut tempor turpis non dolor feugiat.</p>

  <h2 class="abs section-title" style="top:484px">Lorem Ipsum Title</h2>
  <div class="abs rule" style="top:512px"></div>
  <p class="abs copy" style="top:524px">Fusce quis lacus diam, sit amet sollicitudin ante. Quisque ultricies dolor sit amet enim malesuada consectetur. Maecenas vulputate tellus nec orci posuere interdum. Suspendisse potenti. Fusce qis enim massa. Ut tempor turpis non dolor feugiat vel tempus ligula malesuada nibh erat, euismod ac interdum non, lacinia eu massa. Maecenas vulputate tellus nec orci posuere interdum. Suspendisse potenti. Fusce qis enim massa. Ut tempor turpis non dolor feugiat.</p>

  <h2 class="abs section-title" style="top:605px">How We Work</h2>
  <div class="abs photo" role="img" aria-label="Blue-toned photo of a pen tracing a line chart on a printed financial report"></div>

  <ul class="checks">
    <li style="top:639px"><svg width="15" height="12" viewBox="0 0 15 12" aria-hidden="true"><polyline points="1.5,6 5.5,10 13.5,1.5" fill="none" stroke="#f29b00" stroke-width="2.6"/></svg>Fusce quis lacus diam, sit amet sollicitudin</li>
    <li style="top:659px"><svg width="15" height="12" viewBox="0 0 15 12" aria-hidden="true"><polyline points="1.5,6 5.5,10 13.5,1.5" fill="none" stroke="#f29b00" stroke-width="2.6"/></svg>Quisque ultricies dolor sit amet enim malesuada</li>
    <li style="top:679px"><svg width="15" height="12" viewBox="0 0 15 12" aria-hidden="true"><polyline points="1.5,6 5.5,10 13.5,1.5" fill="none" stroke="#f29b00" stroke-width="2.6"/></svg>Maecenas vulputate tellus nec orci posuere</li>
    <li style="top:699px"><svg width="15" height="12" viewBox="0 0 15 12" aria-hidden="true"><polyline points="1.5,6 5.5,10 13.5,1.5" fill="none" stroke="#f29b00" stroke-width="2.6"/></svg>Suspendisse potenti eusce qis enim massa</li>
    <li style="top:719px"><svg width="15" height="12" viewBox="0 0 15 12" aria-hidden="true"><polyline points="1.5,6 5.5,10 13.5,1.5" fill="none" stroke="#f29b00" stroke-width="2.6"/></svg>Ut tempor turpis non dolor feugiat</li>
    <li style="top:739px"><svg width="15" height="12" viewBox="0 0 15 12" aria-hidden="true"><polyline points="1.5,6 5.5,10 13.5,1.5" fill="none" stroke="#f29b00" stroke-width="2.6"/></svg>Maecenas vulputate tellus nec orci posure</li>
    <li style="top:759px"><svg width="15" height="12" viewBox="0 0 15 12" aria-hidden="true"><polyline points="1.5,6 5.5,10 13.5,1.5" fill="none" stroke="#f29b00" stroke-width="2.6"/></svg>Suspendisse potenti qis enim massa</li>
  </ul>
</main>

<section class="partners">
  <div class="abs rule-bottom"></div>
  <div class="abs partner" style="left:124px"><i></i>Meridia Lines</div>
  <div class="abs partner" style="left:296px"><i></i>Tidewell</div>
  <div class="abs partner" style="left:403px"><i></i>Crestfield Cargo</div>
  <div class="abs partner" style="left:590px"><i></i>Norrholm Freight</div>
  <div class="abs partner" style="left:746px"><i></i>Baywick Shipping</div>
</section>

<footer>
  <div class="abs footer"></div>
  <nav class="footer-nav">
    <a href="#" style="left:102px">ABOUT US</a>
    <a href="#" style="left:172px">HOW WE WORK</a>
    <a href="#" style="left:272px">OUR SERVICES</a>
    <a href="#" style="left:360px">WHY NAUTIVEX</a>
    <a href="#" style="left:464px">NEWS AND UPDATES</a>
  </nav>
  <div class="abs footer-mark" aria-hidden="true"></div>
  <div class="abs footer-name">The Harbourline Shipping Association</div>
  <div class="abs copyright">© Copyright 2012. All Rights Reserved.</div>

  <h3 class="abs connect-title" style="font-weight:400">Connect With Us</h3>
  <div class="abs feed">
    Praesent tempus sagittis elementum. Prsent id quam erat, sit amet condimentum neque. Phasellus quis est nisi. Ut luctus adipiscing.
    <div class="feed-meta">Lorem Ipsum <em>2 hours ago</em></div>
  </div>
  <a class="abs social" href="#" style="left:686px" aria-label="Professional network"></a>
  <a class="abs social" href="#" style="left:715px" aria-label="Community page"></a>
  <a class="abs social" href="#" style="left:745px" aria-label="Social page"></a>
  <a class="abs social" href="#" style="left:775px" aria-label="News feed"></a>
</footer>

</body>
</html>
```